New business card for a regional office of a US M&A company

We need business card for a finance company, office based in Hong Kong , our Head office is in US, our business is to Merge and acquires companies , the new office will be a regional office for the Asia Pacific region. We want to use the head office logo as attached ( but don't have to be exactly the same, can be a variation to it) as a base and then add Asia Pacific alongside the logo.
We would prefer to have be bilingual Eng + Chinese, although we don't really have Chinese company name .

Industry/Entity Type

Business

Contact Information for Business Card

Clara Ruth Lindqvist
 

VP,
APAC M&A Operations
Oran Meridian Asia Pacific Limited
 
Unit 1807, K28
14 Tai Lok Fung Road, 
Hong Kong 
 
M: +852 6418 2074
T : +852 2836 4100
F : +852 2836 4177
VOIP: 4815
 
crlindqvist@oranmeridian.com

Font styles to use
Serif
Sans Serif

Colors

Designer to choose colors to be used in the design.

Requirements
Must have
• APAC Office

```html
<!DOCTYPE html>
<html lang="en">
<head>
<meta charset="utf-8">
<title>Oran Meridian Asia Pacific – Business Card</title>
<link href="https://fonts.googleapis.com/css2?family=Montserrat:ital,wght@0,700;1,400&family=Lato:wght@400&family=Encode+Sans+Condensed:wght@400;700&display=swap" rel="stylesheet">
<style>
  :root {
    --navy: #0f2842;
    --cyan: #1fa9d1;
    --paper: #ffffff;
    --panel-grey: #e6e6e6;
    --backdrop: #dcdcdc;
    --ink: #3b3b3b;
    --white: #ffffff;
  }
  html, body {
    margin: 0;
    padding: 0;
    width: 1200px;
    height: 1200px;
    overflow: hidden;
    background: var(--backdrop);
  }
  .canvas { position: relative; width: 1200px; height: 1200px; }

  .card {
    position: absolute;
    width: 656px;
    height: 374px;
    overflow: hidden;
  }

  /* Front */
  .card-front { left: 273px; top: 153px; background: var(--paper); }
  .front-mark {
    position: absolute; left: 308px; top: 72px;
    width: 40px; height: 40px; background: var(--navy);
  }
  .brand-name {
    position: absolute; left: 0; width: 100%; text-align: center;
    font-family: "Montserrat", sans-serif; font-weight: 700;
    color: var(--cyan); letter-spacing: 1px; margin: 0;
  }
  .card-front .brand-name { top: 162px; font-size: 42px; line-height: 54px; }
  .brand-region {
    position: absolute; left: 0; width: 100%;
    display: flex; justify-content: center; align-items: center;
    font-family: "Montserrat", sans-serif; font-style: italic; font-weight: 400;
    color: var(--ink);
  }
  .brand-region .dash { display: inline-block; background: var(--ink); height: 3px; }
  .card-front .brand-region { top: 214px; font-size: 22px; gap: 20px; }
  .card-front .brand-region .dash { width: 26px; }

  .front-band {
    position: absolute; left: 0; bottom: 0; width: 100%; height: 68px;
    background: var(--navy);
  }
  .web-tab { position: absolute; left: 160px; top: 296px; width: 332px; height: 40px; }
  .web-address {
    position: absolute; left: 160px; top: 300px; width: 332px; text-align: center;
    font-family: "Lato", sans-serif; font-size: 23px; color: var(--white);
    letter-spacing: 0.5px;
  }

  /* Back */
  .card-back { left: 274px; top: 664px; background: var(--panel-grey); }
  .back-mark {
    position: absolute; left: 144px; top: 152px;
    width: 34px; height: 34px; background: var(--navy);
  }
  .back-brand { position: absolute; left: 0; top: 0; width: 323px; height: 100%; }
  .back-brand .brand-name { top: 218px; font-size: 27px; line-height: 36px; }
  .back-brand .brand-region { top: 254px; font-size: 16px; gap: 14px; }
  .back-brand .brand-region .dash { width: 16px; height: 2px; }

  .contact-panel {
    position: absolute; left: 323px; top: 0; width: 333px; height: 100%;
    background: var(--navy);
  }
  .icon-strip { position: absolute; left: 317px; top: 144px; width: 38px; height: 214px; }
  .holder-name {
    position: absolute; left: 323px; top: 58px; width: 333px; text-align: center; margin: 0;
    font-family: "Encode Sans Condensed", sans-serif; font-weight: 700;
    font-size: 28px; color: var(--cyan); letter-spacing: -0.3px;
  }
  .holder-title {
    position: absolute; left: 323px; top: 102px; width: 333px; text-align: center;
    font-family: "Lato", sans-serif; font-size: 17px; color: var(--white); letter-spacing: 0.5px;
  }
  .title-rule {
    position: absolute; left: 441px; top: 135px; width: 100px; height: 2px; background: var(--cyan);
  }
  .contact-list {
    position: absolute; left: 372px; top: 184px; margin: 0; padding: 0; list-style: none;
    font-family: "Encode Sans Condensed", sans-serif; font-size: 15px; color: var(--white);
    line-height: 21.5px;
  }
  .contact-list .address-line { line-height: 18px; }
  .contact-list .address-block { margin-bottom: 3px; }
  .contact-list .email { margin-top: 2px; }
</style>
</head>
<body>
<div class="canvas">

  <section class="card card-front" aria-label="Business card front">
    <div class="front-mark" aria-hidden="true"></div>
    <h1 class="brand-name">ORAN MERIDIAN</h1>
    <div class="brand-region"><span class="dash"></span><span>Asia Pacific, LLC</span><span class="dash"></span></div>
    <div class="front-band"></div>
    <svg class="web-tab" viewBox="0 0 332 40" aria-hidden="true">
      <polygon points="0,0 6,0 14,9 6,9" fill="#0a1e33"/>
      <polygon points="332,0 326,0 318,9 326,9" fill="#0a1e33"/>
      <polygon points="6,0 326,0 312,40 20,40" fill="var(--cyan)"/>
    </svg>
    <div class="web-address">www.oranmeridian.com</div>
  </section>

  <section class="card card-back" aria-label="Business card back">
    <div class="back-brand">
      <div class="back-mark" aria-hidden="true"></div>
      <h2 class="brand-name">ORAN MERIDIAN</h2>
      <div class="brand-region"><span class="dash"></span><span>Asia Pacific, LLC</span><span class="dash"></span></div>
    </div>

    <div class="contact-panel"></div>

    <svg class="icon-strip" viewBox="0 0 38 214" aria-hidden="true">
      <polygon points="0,6 6,0 38,12 38,202 6,214 0,208" fill="var(--cyan)"/>
      <!-- pin -->
      <path d="M17 42 C11 34 11 30 11 28 A6 6 0 0 1 23 28 C23 30 23 34 17 42 Z" fill="none" stroke="#fff" stroke-width="1.6"/>
      <circle cx="17" cy="28" r="2" fill="none" stroke="#fff" stroke-width="1.4"/>
      <!-- phone -->
      <path d="M12 82 C12 80 14 79 15 80 L17 83 C17.5 84 17 85 16 85.5 C16.5 88 18 90 20.5 91 C21 90 22 89.5 23 90 L25.5 92 C26.5 93 25.5 95 23.5 95 C17 94.5 12.5 89 12 82 Z" fill="#fff"/>
      <!-- mail -->
      <rect x="10" y="171" width="15" height="10" fill="none" stroke="#fff" stroke-width="1.4"/>
      <polyline points="10,171 17.5,177 25,171" fill="none" stroke="#fff" stroke-width="1.4"/>
      <line x1="10" y1="181" x2="15.5" y2="176" stroke="#fff" stroke-width="1.2"/>
      <line x1="25" y1="181" x2="19.5" y2="176" stroke="#fff" stroke-width="1.2"/>
    </svg>

    <h3 class="holder-name">CLARA RUTH LINDQVIST</h3>
    <div class="holder-title">Vice President</div>
    <div class="title-rule"></div>

    <ul class="contact-list">
      <li class="address-block">
        <div class="address-line">Unit 1807, K28</div>
        <div class="address-line">14 Tai Lok Fung Road,&nbsp; Hong Kong</div>
      </li>
      <li>M: +852 6418 2074</li>
      <li>T : +852 2836 4100</li>
      <li>F : +852 2836 4177</li>
      <li>VOIP: 4815</li>
      <li class="email">crlindqvist@oranmeridian.com</li>
    </ul>
  </section>

</div>
</body>
</html>
```